Business Card for a Mortgage Agent (myself)

I need a business card for my new job as Mortgage Agent. The Broker's logo is to be on the card as well as the brokerage License number. Not sure if to include a photo or not. Info to be on card.
Dante Roux
Mortgage Agent
Lic # M47105386
Cell: 905-614-2753
Email: danterouxk.ma@fennmail.com
Web: www.karlvostermortgages.com
TPW Brokerage Lic. # 73918

```html
<!DOCTYPE html>
<html lang="en">
<head>
<meta charset="utf-8">
<title>TPW Mortgage Agent Business Card – Dante Roux</title>
<link rel="stylesheet" href="https://fonts.googleapis.com/css2?family=Figtree:wght@400;500;600;700&family=Source+Serif+4:opsz,wght@8..60,600&display=swap">
<style>
  :root {
    --navy: #262e78;
    --yellow: #ebbd0c;
    --paper: #ececec;
    --ink: #4a4a4a;
    --backdrop: #dcdcdc;
  }
  * { margin: 0; padding: 0; box-sizing: border-box; }
  html, body {
    width: 1200px; height: 896px; overflow: hidden;
    background: var(--backdrop);
    font-family: "Figtree", sans-serif;
  }
  .card {
    position: absolute; left: 336px;
    width: 524px; height: 299px;
    box-shadow: 0 14px 22px rgba(0,0,0,0.18);
    overflow: hidden;
  }
  .card--front { top: 126px; background: var(--navy); }
  .card--back { top: 475px; background: var(--paper); }

  /* Front */
  .front-mark {
    position: absolute; left: 0; right: 0; top: 96px;
    display: flex; align-items: center; justify-content: center; gap: 18px;
  }
  .front-mark__square { width: 34px; height: 34px; background: var(--yellow); }
  .front-mark__name {
    font-weight: 700; font-size: 64px; letter-spacing: 18px;
    color: #fff; line-height: 1;
  }
  .front-licence {
    position: absolute; top: 228px; right: 130px;
    font-size: 8px; font-style: italic; color: #fff; letter-spacing: 0.3px;
  }

  /* Back */
  .back-mark {
    position: absolute; left: 52px; width: 191px; top: 112px;
    display: flex; align-items: center; justify-content: center; gap: 12px;
  }
  .back-mark__square { width: 22px; height: 22px; background: var(--yellow); }
  .back-mark__name {
    font-weight: 700; font-size: 40px; letter-spacing: 10px;
    color: var(--navy); line-height: 1;
  }
  .back-licence {
    position: absolute; left: 52px; width: 191px; top: 178px;
    text-align: center; font-size: 6px; font-style: italic; color: var(--navy);
  }
  .divider {
    position: absolute; left: 262px; top: 78px;
    width: 1px; height: 132px; background: var(--navy);
  }
  .agent { position: absolute; left: 281px; top: 76px; color: var(--ink); }
  .agent__name {
    font-family: "Source Serif 4", serif; font-weight: 600;
    font-size: 23px; color: var(--navy); line-height: 1.1;
  }
  .agent__line { font-size: 11.6px; line-height: 16.5px; }
  .agent__role { margin-bottom: 6px; }
  .agent__address { margin-bottom: 7px; }
  .agent__label { color: var(--navy); font-weight: 600; }

  .footer-bands { position: absolute; left: 0; bottom: 0; }
  .web {
    position: absolute; right: 30px; top: 273px;
    font-size: 12px; color: #fff;
  }
  .web__domain { color: var(--yellow); font-weight: 600; }
</style>
</head>
<body>

<section class="card card--front" aria-label="Card front">
  <div class="front-mark">
    <span class="front-mark__square"></span>
    <span class="front-mark__name">TPW</span>
  </div>
  <p class="front-licence">License #73918</p>
</section>

<section class="card card--back" aria-label="Card back">
  <div class="back-mark">
    <span class="back-mark__square"></span>
    <span class="back-mark__name">TPW</span>
  </div>
  <p class="back-licence">License #73918</p>

  <div class="divider"></div>

  <div class="agent">
    <h1 class="agent__name">Dante Roux</h1>
    <p class="agent__line agent__role">Mortgage Agent - M47105386</p>
    <p class="agent__line agent__address">318 Garnet Street, West<br>London, Ontario N6J 2R7</p>
    <p class="agent__line"><span class="agent__label">Cell:</span> 905-614-2753</p>
    <p class="agent__line"><span class="agent__label">Email:</span> danterouxk.ma@fennmail.com</p>
    <p class="agent__line"><span class="agent__label">TPW Brokerage Lic.</span> # 73918</p>
  </div>

  <svg class="footer-bands" width="524" height="299" viewBox="0 0 524 299">
    <polygon points="287,266 524,266 524,299 273,299" fill="var(--navy)"/>
    <polygon points="0,278 281,278 277,285 0,285" fill="var(--yellow)"/>
    <rect x="0" y="289" width="290" height="10" fill="var(--navy)"/>
  </svg>
  <p class="web">www.<span class="web__domain">karlvostermortgages</span>.com</p>
</section>

</body>
</html>
```